Author book covers needed for a spiritual book, eastern wisdom

I need a cover for a 'Anthology'. I'm an author and I have established myself in a genre of its own, a symbiosis between spirituality and literature. My books are always a mix of entertainment and depth. Many of my readers have highlighted in the now eight books I have written many passages and asked me if it was not possible to collect all the wisdom, quotes, sayings and stories in a volume of aphorisms. I did this. Worker Title: "Willow of quiet rain ... to carry your days toward a calm shore" Seeking a cover that this gold dust elements and at the same time combines the possibility of transformation and a bit mystical. .. Mainly it's in my books to eastern philosophies, ie Buddhism, Upanishads, the Vedas ... the Yoga Vasishta, the Bhagavad Gita and the like A variable template I found at pixmerra - but it is not a must, if anyone has a better has idea. Be creative! My author name: Marveta Lonchiro greetings Marveta Lonchiro

Target Market(s)

People who are spiritually interested and concerned about their lives make the book to be traded as a gift - and thus look accordingly.

Requirements
Must have
• a spiritual touch - spiritual touch if possible - a gift-character, so did customers feel inspired to give the book as a present to friends and relatives or other people. Please place the author's name at the lower end.
Nice to have
• Gold particles and Luminiscence ... to express did the word inside the book hopefully lighten up ones heart, to illumine ones soul or to help through a critical situation. So to say, bring some gold into a dark world ...
Should not have
• pls no black cover

```html
<!DOCTYPE html>
<html lang="en">
<head>
<meta charset="utf-8">
<title>Willow of Quiet Rain – Cover Wrap</title>
<link rel="stylesheet" href="https://fonts.googleapis.com/css2?family=Cinzel+Decorative:wght@400&family=EB+Garamond:wght@400&display=swap">
<style>
  :root {
    --midnight: #140f2e;
    --midnight-deep: #0e0a22;
    --indigo-haze: rgba(70, 50, 120, 0.55);
    --ink-light: #f4f0e6;
    --gold-bright: rgba(226, 190, 110, 0.62);
    --gold-soft: rgba(196, 160, 82, 0.42);
    --gold-faint: rgba(176, 140, 70, 0.22);
    --warm-skin: rgba(190, 140, 100, 0.55);
    --label-white: #ffffff;
  }
  * { margin: 0; padding: 0; box-sizing: border-box; }
  html, body { width: 1200px; height: 864px; overflow: hidden; background: var(--midnight-deep); }
  .wrap {
    position: relative;
    width: 1200px;
    height: 864px;
    background: linear-gradient(160deg, var(--midnight-deep) 0%, var(--midnight) 55%, #1b1338 100%);
    color: var(--ink-light);
    overflow: hidden;
  }
  .dust-artwork {
    position: absolute;
    left: 460px;
    top: 170px;
    width: 740px;
    height: 694px;
    background:
      radial-gradient(ellipse 90px 150px at 360px 330px, var(--warm-skin), transparent 80%),
      radial-gradient(ellipse 260px 220px at 340px 260px, var(--gold-bright), transparent 70%),
      radial-gradient(ellipse 400px 330px at 330px 300px, var(--gold-soft), transparent 75%),
      radial-gradient(ellipse 520px 420px at 360px 320px, var(--gold-faint), transparent 82%),
      radial-gradient(ellipse 560px 460px at 460px 360px, var(--indigo-haze), transparent 85%);
  }
  .display {
    font-family: "Cinzel Decorative", serif;
    font-weight: 400;
    color: var(--ink-light);
    white-space: nowrap;
  }
  .back-title {
    position: absolute;
    left: 78px;
    width: 444px;
    top: 48px;
    text-align: center;
    font-size: 24px;
  }
  .blurb {
    position: absolute;
    left: 78px;
    top: 94px;
    width: 444px;
    font-family: "EB Garamond", serif;
    font-size: 14.2px;
    line-height: 17.6px;
    text-align: justify;
    hyphens: auto;
  }
  .blurb p + p { margin-top: 17.6px; }
  .barcode-label {
    position: absolute;
    left: 75px;
    top: 712px;
    width: 145px;
    height: 106px;
    background: var(--label-white);
  }
  .spine-title, .spine-author {
    position: absolute;
    left: 596px;
    transform-origin: 0 0;
    transform: rotate(90deg) translateY(-50%);
  }
  .spine-title { top: 186px; font-size: 20px; }
  .spine-author { top: 640px; font-size: 18px; }
  .front-title {
    position: absolute;
    left: 640px;
    width: 552px;
    top: 40px;
    text-align: center;
    font-size: 42px;
  }
  .front-subtitle {
    position: absolute;
    left: 640px;
    width: 552px;
    top: 126px;
    text-align: center;
    font-size: 20px;
  }
  .front-author {
    position: absolute;
    left: 640px;
    width: 552px;
    top: 768px;
    text-align: center;
    font-size: 45px;
  }
</style>
</head>
<body>
<main class="wrap">
  <div class="dust-artwork" role="img" aria-label="Photograph of a hand flicking luminous gold dust that scatters across the midnight background"></div>

  <section class="back-cover">
    <h2 class="display back-title">Willow of Quiet Rain</h2>
    <div class="blurb">
      <p>Lorem ipsum dolor sit amet, consectetur adipiscing elit. Pellentesque faucibus nunc felis, sit amet efficitur leo viverra nec. Proin dapibus sodales sem ut hendrerit. Morbi scelerisque ac tellus ut dignissim. Donec et sodales neque. Cras vel magna lectus. Ut et magna elementum, pharetra nisi in, egestas sapien. Suspendisse malesuada vulputate ultrices.</p>
      <p>Nam est magna, iaculis ac bibendum vitae, convallis a sem. Aliquam vitae dolor mi. Nam rhoncus nibh in turpis bibendum convallis. Proin congue erat id tortor rutrum, quis rutrum tellus vulputate. Nullam augue lectus, accumsan in felis quis, ultricies pellentesque arcu. In convallis vitae turpis ut luctus. Praesent porta mattis lectus, non semper justo mollis quis. Etiam luctus, diam et lacinia pulvinar, urna dui elementum lectus, rutrum rutrum neque justo quis neque. Mauris vitae blandit elit. Nullam vitae massa elementum, fringilla tellus et, porta ex. Praesent convallis pretium odio. Vestibulum eget fermentum sapien. Morbi mattis lectus in odio venenatis, ac consectetur leo elementum.</p>
      <p>Maecenas a nisl ex. Suspendisse est orci, tempor ut neque ac, pellentesque faucibus leo. Aenean tempus rutrum tempor. Ut laoreet commodo dui, a tincidunt velit elementum vel. Proin mattis posuere lacus, gravida posuere turpis. Proin eu malesuada justo. Quisque vehicula scelerisque urna vel varius. Vestibulum sed dapibus ipsum. Praesent rutrum tortor eget mauris mattis, eu ullamcorper arcu placerat. Proin nulla turpis, sagittis a turpis pretium, porta congue risus. Suspendisse tellus lorem, ornare non sem in, luctus lacinia mauris. Class aptent taciti sociosqu ad litora torquent per conubia nostra, per inceptos himenaeos. Donec ullamcorper, enim eget maximus porttitor, libero tortor consectetur arcu, quis accumsan metus arcu vitae elit. Curabitur mollis mollis varius.</p>
    </div>
    <div class="barcode-label"></div>
  </section>

  <section class="spine">
    <span class="display spine-title">Willow of Quiet Rain</span>
    <span class="display spine-author">Marveta Lonchiro</span>
  </section>

  <section class="front-cover">
    <h1 class="display front-title">Willow of Quiet Rain</h1>
    <p class="display front-subtitle">To carry your days toward a calm shore</p>
    <p class="display front-author">Marveta Lonchiro</p>
  </section>
</main>
</body>
</html>
```